Business cards for education company

We need a business card design for a relatively new company based in Queensland and operating across Australia. We resell diploma level education courses which include Business, Management, Finance, Community Services & Government courses. We offer over 20 different courses.
The target market is for anyone 16 years of age and older. There is no age limit.

We would like to see the design use the color blue and silver. The final design should communicate professionalism and a bright future.

We sell education but are also promoting the career they see themselves in 2-3 years in the future

Our company logo is attached.

Target Market(s)

We target all age groups above 16 years of age. The main target market would be people aged between 17-35.

We focus on those people who cannot make it into University or do not want to commit the time to a full degree.

Industry/Entity Type

Education

Requirements
Must have
• Professional
Company logo
website
Contact details:

Please use the following example:

Lionel Parfitt
Senior Education Consultant
0417 386 591
Lionel.parfitt@brightwaylearninghub.com.au
www.brightwaylearninghub.com.au

```html
<!DOCTYPE html>
<html lang="en">
<head>
<meta charset="utf-8">
<title>Brightway Learning Hub – Business Cards</title>
<link rel="stylesheet" href="https://fonts.googleapis.com/css2?family=Arimo:wght@400;700&display=swap">
<style>
  :root {
    --backdrop: #d9d6d1;
    --card-blue: #5aa3d8;
    --card-silver: #ececec;
    --navy: #173f7a;
    --brand-blue: #1f5fa8;
    --accent-blue: #2a7fd0;
    --text-grey: #4a4a4a;
    --white: #ffffff;
  }
  * { box-sizing: border-box; margin: 0; padding: 0; }
  html, body {
    width: 1200px; height: 900px; overflow: hidden;
    background: var(--backdrop);
    font-family: "Arimo", Arial, sans-serif;
  }
  .sheet {
    width: 1200px; height: 900px;
    display: flex; flex-direction: column; align-items: center; justify-content: center;
    gap: 56px;
  }
  .card {
    width: 580px; height: 354px; position: relative;
    box-shadow: 0 6px 18px rgba(0,0,0,.18);
  }
  .card--front { background: var(--card-blue); }
  .card--back { background: var(--card-silver); }

  .front-brand {
    position: absolute; top: 110px; left: 0; right: 0;
    display: flex; align-items: center; justify-content: center; gap: 14px;
  }
  .brand-dot { width: 26px; height: 26px; border-radius: 50%; background: var(--navy); }
  .brand-name {
    font-weight: 700; font-size: 30px; letter-spacing: 1px;
    text-transform: uppercase; color: var(--navy);
  }
  .tagline {
    position: absolute; top: 214px; right: 96px;
    background: var(--navy); color: var(--white);
    font-size: 17px; padding: 8px 28px 8px 18px;
    clip-path: polygon(0 0, 94% 0, 100% 50%, 94% 100%, 0 100%);
  }

  .back-brand {
    position: absolute; top: 54px; left: 44px;
    display: flex; align-items: center; gap: 12px;
  }
  .back-brand .brand-name { font-size: 26px; color: var(--brand-blue); }
  .back-brand .brand-dot { width: 22px; height: 22px; background: var(--brand-blue); }

  .person { position: absolute; top: 150px; left: 44px; color: var(--text-grey); }
  .person__name { font-size: 24px; letter-spacing: .5px; text-transform: uppercase; }
  .person__title { font-size: 17px; margin-top: 4px; }

  .contact { position: absolute; top: 248px; left: 44px; list-style: none; color: var(--text-grey); font-size: 15px; }
  .contact li { display: flex; align-items: center; gap: 12px; height: 24px; }
  .contact svg { width: 14px; height: 14px; fill: var(--accent-blue); flex: none; }
  .contact .web-name { color: var(--accent-blue); font-weight: 700; }
</style>
</head>
<body>
<main class="sheet">
  <section class="card card--front" aria-label="Card front">
    <div class="front-brand">
      <span class="brand-dot"></span>
      <span class="brand-name">Brightway Learning Hub</span>
    </div>
    <p class="tagline">Your next step to a brighter future!</p>
  </section>

  <section class="card card--back" aria-label="Card back">
    <div class="back-brand">
      <span class="brand-dot"></span>
      <span class="brand-name">Brightway Learning Hub</span>
    </div>
    <div class="person">
      <p class="person__name">Lionel Parfitt</p>
      <p class="person__title">Senior Education Consultant</p>
    </div>
    <ul class="contact">
      <li>
        <svg viewBox="0 0 14 14" aria-hidden="true"><path d="M3 0h8a1 1 0 0 1 1 1v12a1 1 0 0 1-1 1H3a1 1 0 0 1-1-1V1a1 1 0 0 1 1-1zm1 2v8h6V2z"/></svg>
        <span>0417 386 591</span>
      </li>
      <li>
        <svg viewBox="0 0 14 14" aria-hidden="true"><path d="M0 3h14v9H0zm1 1v.4l6 4 6-4V4z"/></svg>
        <span>Lionel.parfitt@brightwaylearninghub.com.au</span>
      </li>
      <li>
        <svg viewBox="0 0 14 14" aria-hidden="true"><path d="M7 0a5 5 0 0 1 5 5c0 3.5-5 9-5 9S2 8.5 2 5a5 5 0 0 1 5-5zm0 3a2 2 0 1 0 0 4 2 2 0 0 0 0-4z"/></svg>
        <span>www.<span class="web-name">brightwaylearninghub</span>.com.au</span>
      </li>
    </ul>
  </section>
</main>
</body>
</html>
```